Kivo Commercial Cleaning is lookong for a new business card design.

A fresh new design that's professional and stylish. We need a serious upgrade to our business cards. I have included pictures of our existing ones. Our clients include professional individuals and business owners. We woupdblike something professional and upbeat. Please have fun and see what you come uo with.

Target Market(s)

Property managers, business owners, facility managers and other similar professionals

Industry/Entity Type

Janitorial

Contact Information for Business Card

Name, cell, office number, email, web address

Font styles to use
Sans Serif

Colors

Designer to choose colors to be used in the design.

Requirements
Must have
• please use the green color in our logo
Nice to have
• Bar code
Should not have
• Address

```html
<!DOCTYPE html>
<html lang="en">
<head>
<meta charset="utf-8">
<title>Kivo Commercial Cleaning — Business Card</title>
<link href="https://fonts.googleapis.com/css2?family=Quicksand:wght@700&family=Raleway:wght@400;500;600&display=swap" rel="stylesheet">
<style>
  :root {
    --brand-green: #00b74f;
    --brand-blue: #0068ad;
    --paper: #ffffff;
    --backdrop: #e9ebea;
  }
  * { margin: 0; padding: 0; box-sizing: border-box; }
  html, body {
    width: 1200px; height: 1200px; overflow: hidden;
    background: var(--backdrop);
  }
  .card {
    position: absolute;
    left: 160px;
    width: 880px; height: 503px;
    border-radius: 34px;
    overflow: hidden;
    box-shadow: 0 6px 18px rgba(0,0,0,.15);
  }
  .card--front { top: 60px; background: var(--brand-green); }
  .card--back { top: 637px; background: var(--brand-green); }

  .front-shapes { position: absolute; inset: 0; }

  .wordmark {
    position: absolute;
    font-family: 'Quicksand', sans-serif;
    font-weight: 700;
    line-height: 1;
  }
  .wordmark__name { display: block; }
  .wordmark__descriptor { display: block; letter-spacing: .01em; }

  .card--front .wordmark {
    left: 70px; top: 178px;
    color: var(--brand-green);
  }
  .card--front .wordmark__name { font-size: 120px; letter-spacing: -.01em; }
  .card--front .wordmark__descriptor { font-size: 25px; margin-top: 8px; padding-left: 4px; color: var(--brand-blue); }

  .contact {
    position: absolute;
    left: 552px; top: 150px;
    color: var(--paper);
    font-family: 'Raleway', sans-serif;
  }
  .contact__name {
    font-size: 30px; font-weight: 600;
    letter-spacing: .02em; text-transform: uppercase;
    margin-bottom: 18px;
  }
  .contact__list { list-style: none; }
  .contact__item {
    display: flex; align-items: center; gap: 10px;
    font-size: 20px; font-weight: 400;
    line-height: 1.55;
  }
  .contact__icon { width: 18px; height: 18px; flex: none; }

  .card--back .wordmark {
    left: 0; right: 0; top: 150px;
    text-align: center;
    color: var(--paper);
  }
  .card--back .wordmark__name { font-size: 170px; letter-spacing: -.01em; }
  .card--back .wordmark__descriptor { font-size: 36px; margin-top: 10px; }
</style>
</head>
<body>

<section class="card card--front" aria-label="Business card, front">
  <svg class="front-shapes" viewBox="0 0 880 503" width="880" height="503" aria-hidden="true">
    <path d="M0 0 H356 C496 40 566 300 456 503 H0 Z" fill="var(--paper)"/>
    <path d="M0 0 H348 C488 40 558 300 448 503 H0 Z" fill="var(--brand-blue)"/>
    <path d="M0 0 H330 C468 44 530 300 426 503 H0 Z" fill="var(--paper)"/>
  </svg>

  <div class="wordmark">
    <span class="wordmark__name">Kivo</span>
    <span class="wordmark__descriptor">commercial cleaning</span>
  </div>

  <div class="contact">
    <h1 class="contact__name">Jamie Corlett</h1>
    <ul class="contact__list">
      <li class="contact__item">
        <svg class="contact__icon" viewBox="0 0 24 24" aria-hidden="true"><path fill="#fff" d="M6.6 10.8a15.1 15.1 0 0 0 6.6 6.6l2.2-2.2c.3-.3.7-.4 1-.2 1.1.4 2.3.6 3.6.6.6 0 1 .4 1 1V20c0 .6-.4 1-1 1A17 17 0 0 1 3 4c0-.6.4-1 1-1h3.5c.6 0 1 .4 1 1 0 1.3.2 2.5.6 3.6.1.3 0 .7-.2 1z"/></svg>
        (555) 014-2273
      </li>
      <li class="contact__item">
        <svg class="contact__icon" viewBox="0 0 24 24" aria-hidden="true"><path fill="#fff" d="M2 5h20v14H2z"/><path fill="none" stroke="var(--brand-green)" stroke-width="1.8" d="M2 5l10 8 10-8M2 19l7.5-7M22 19l-7.5-7"/></svg>
        jamie@kivocleaning.com
      </li>
      <li class="contact__item">
        <svg class="contact__icon" viewBox="0 0 24 24" aria-hidden="true"><g fill="none" stroke="#fff" stroke-width="1.8"><circle cx="12" cy="12" r="10"/><ellipse cx="12" cy="12" rx="4.5" ry="10"/><path d="M2 12h20M4 7h16M4 17h16"/></g></svg>
        www.kivocleaning.com
      </li>
    </ul>
  </div>
</section>

<section class="card card--back" aria-label="Business card, back">
  <div class="wordmark">
    <span class="wordmark__name">Kivo</span>
    <span class="wordmark__descriptor">commercial cleaning</span>
  </div>
</section>

</body>
</html>
```